Art Deco Wedding Invitation

We need a wedding invitation designed for a 1920's Art Deco theme.
The wedding will take place in Berlin, which had a glamorous, modern and wild culture in the 1920's. This may offer some design inspiration.
The couple's names are Rowland and Liora and the wedding will take place on May 8, 2015.

Industry/Entity Type

Wedding

```html
<!DOCTYPE html>
<html lang="en">
<head>
<meta charset="utf-8">
<title>Rowland &amp; Liora – 1920's Wedding Invitation</title>
<link rel="stylesheet" href="https://fonts.googleapis.com/css2?family=Pinyon+Script&family=Cormorant+Garamond:ital,wght@1,500&display=swap">
<style>
  :root {
    --paper: #ffffff;
    --ink: #111111;
    --gold-deep: #b8992f;
    --gold-mid: #d6b24e;
    --gold-light: #fff5c4;
    --page-edge: #9a9a9a;
    --script: "Pinyon Script", cursive;
    --serif: "Cormorant Garamond", serif;
  }
  html, body { margin: 0; padding: 0; overflow: hidden; background: var(--paper); }
  .invitation { position: relative; width: 1200px; height: 909px; background: var(--paper); overflow: hidden; }
  .invitation__art { position: absolute; inset: 0; }
  .cover__title, .cover__year, .cover__to, .message, .couple, .details { position: absolute; margin: 0; color: var(--ink); text-align: center; font-weight: 400; white-space: nowrap; }
  .cover__title { left: 160px; width: 280px; top: 302px; font-family: var(--script); font-size: 56px; line-height: 1; }
  .cover__year { left: 200px; width: 200px; top: 380px; font-family: var(--script); font-size: 30px; line-height: 1; }
  .cover__to { left: 157px; top: 528px; font-family: var(--script); font-size: 34px; line-height: 1; text-align: left; }
  .message { font-family: var(--serif); font-style: italic; }
  .message--intro { top: 141px; left: 758px; width: 300px; font-size: 33px; line-height: 38px; }
  .message--era { top: 262px; left: 776px; width: 300px; font-family: var(--script); font-style: normal; font-size: 50px; line-height: 1; }
  .message--guest { top: 316px; left: 807px; width: 260px; font-size: 25px; line-height: 28px; }
  .couple { left: 830px; width: 244px; top: 382px; font-family: var(--script); font-size: 52px; line-height: 48px; }
  .details { left: 805px; width: 280px; top: 550px; font-family: var(--serif); font-style: italic; font-size: 31px; line-height: 37px; }
</style>
</head>
<body>
<main class="invitation">
  <svg class="invitation__art" width="1200" height="909" viewBox="0 0 1200 909">
    <defs>
      <linearGradient id="gold-sheen" x1="0" x2="1" y1="0" y2="0">
        <stop offset="0" stop-color="#c9a43d"/>
        <stop offset="0.35" stop-color="#e9cd7a"/>
        <stop offset="0.5" stop-color="#fffbe0"/>
        <stop offset="0.7" stop-color="#d4ad4a"/>
        <stop offset="1" stop-color="#c19a35"/>
      </linearGradient>
      <linearGradient id="gold-soft" x1="0" x2="1" y1="0" y2="1">
        <stop offset="0" stop-color="#c9a43d"/>
        <stop offset="0.5" stop-color="#f6e6a8"/>
        <stop offset="1" stop-color="#b8992f"/>
      </linearGradient>
      <linearGradient id="gown-glow" x1="0" x2="1" y1="0" y2="0">
        <stop offset="0" stop-color="#e8cf7f" stop-opacity="0.55"/>
        <stop offset="0.5" stop-color="#fbefc4" stop-opacity="0.7"/>
        <stop offset="1" stop-color="#d9b85a" stop-opacity="0.55"/>
      </linearGradient>
    </defs>

    <rect class="page-edge" x="0.5" y="0.5" width="590" height="893" fill="none" stroke="var(--page-edge)"/>
    <g class="cover-label">
      <rect x="80" y="298" width="428" height="175" fill="url(#gold-sheen)"/>
      <rect x="80" y="298" width="100" height="175" fill="url(#gold-soft)" role="img" aria-label="Art Deco daisy ornament panel"/>
      <rect x="408" y="298" width="100" height="175" fill="url(#gold-soft)" role="img" aria-label="Art Deco daisy ornament panel"/>
      <g stroke="var(--paper)" stroke-width="3">
        <line x1="160" y1="412" x2="430" y2="412"/>
        <line x1="160" y1="424" x2="430" y2="424"/>
        <line x1="160" y1="437" x2="430" y2="437"/>
      </g>
    </g>
    <line class="cover__to-line" x1="207" y1="566" x2="435" y2="566" stroke="var(--ink)" stroke-width="1.2"/>

    <g class="frame" fill="url(#gold-sheen)">
      <rect x="703" y="52" width="16" height="22"/>
      <rect x="728" y="52" width="305" height="20"/>
      <rect x="728" y="80" width="305" height="5"/>
      <rect x="740" y="92" width="293" height="4"/>
      <rect x="703" y="80" width="5" height="740"/>
      <rect x="716" y="92" width="4" height="715"/>
      <rect x="728" y="104" width="4" height="690"/>
      <rect x="740" y="800" width="300" height="5"/>
      <rect x="728" y="812" width="312" height="4"/>
      <rect x="703" y="822" width="16" height="20"/>
      <rect x="728" y="822" width="312" height="20"/>
      <rect x="1136" y="185" width="5" height="530"/>
      <rect x="1146" y="185" width="4" height="530"/>
      <rect x="1155" y="185" width="4" height="530"/>
    </g>
    <path d="M1030 52 H1160 V185 H1090 A60 60 0 0 0 1030 125 Z" fill="url(#gold-soft)" role="img" aria-label="Art Deco corner with daisy ornament"/>
    <path d="M1030 842 H1160 V715 H1090 A60 60 0 0 1 1030 775 Z" fill="url(#gold-soft)" role="img" aria-label="Art Deco corner with daisy ornament"/>
    <g stroke="var(--gold-deep)" stroke-width="3">
      <line x1="858" y1="370" x2="1042" y2="370"/>
      <line x1="850" y1="535" x2="1042" y2="535"/>
    </g>

    <rect class="bride-illustration" x="598" y="260" width="208" height="535" rx="40" fill="url(#gown-glow)" role="img" aria-label="Illustration of a 1920s bride in a flowing gold gown holding a daisy bouquet"/>
  </svg>

  <p class="cover__title">Invitation</p>
  <p class="cover__year">1920's</p>
  <p class="cover__to">To:</p>

  <p class="message message--intro">Friends, let’s go back<br>the time, glamorous,<br>modern and wild ...</p>
  <p class="message message--era">1920's</p>
  <p class="message message--guest">Please be our guest as we,</p>
  <h1 class="couple">Rowland<br>and<br>Liora</h1>
  <p class="details">join together<br>on May 8, 2015.<br>Lindenhof Chapel<br>Ahornweg Road<br>Berlin, Germany</p>
</main>
</body>
</html>
```